Travel Poster Design Project

A poster design for a specific Adventure Travel Journey to Ladakh India. The journey it will be promoting is a 2 week trekking and cultural tour through Ladakh passing over 2 mountain passes in excess of 5000 meters.

Dates are July and August each year

Brand Name is Far Ridge Voyages

We do inspiring unique journeys in a small select number of locations around the world. Ladakh is also known as Little Tibet and has a buddhist culture

We have a logo already to use and we also have a range of photos online for you to select from. They can be seen at http://photos.brookcanoe.example/FarRidgeVoyages then click on Ladakh

Target Market(s)

Adventure travel people 30-55 poster will be displayed in our rafting retail base so will be seen by target market

Industry/Entity Type

Travel

Requirements
Must have
• website address www.farridgevoyages.example
Phone Number 01632 960418
email info@farridgevoyages.example
Pictures
small legal note along the bottom, saying Far Ridge Voyages is a brand name of Torrent Bend Paddle Outfitters LLP
Nice to have
• Lots of inspiring photos and colour
Should not have
• named dates

```html
<!DOCTYPE html>
<html lang="en">
<head>
<meta charset="utf-8">
<title>Far Ridge Voyages — Ladakh Poster</title>
<link rel="stylesheet" href="https://fonts.googleapis.com/css2?family=Montserrat:ital,wght@0,300;0,400;0,700;0,800;1,700&display=swap">
<style>
  :root {
    --ink: #1c3f95;
    --muted: #8a8f99;
    --paper: #ffffff;
    --stage: #ffffff;
    --edge: #d6d6d6;
    --sky: #2f6fd0;
    --snow: #e4e6ea;
    --rock: #b59b80;
    --flag-a: #d8453b;
    --flag-b: #3b8c4a;
    --flag-c: #f2c230;
    --stone: #a88c6c;
    --mural: #d8572a;
    --band-blue: #4fa3d9;
    --band-gold: #d9a23a;
  }
  * { box-sizing: border-box; margin: 0; padding: 0; }
  html, body {
    width: 1200px; height: 900px; overflow: hidden;
    background: var(--stage);
    font-family: "Montserrat", Arial, sans-serif;
    color: var(--ink);
  }
  .poster {
    position: absolute; left: 308px; top: 37px;
    width: 586px; height: 830px;
    background: var(--paper);
    border: 1px solid var(--edge);
  }
  .side-band {
    position: absolute; right: 0; top: 0; width: 78px; height: 100%;
    background: linear-gradient(90deg, var(--band-blue) 0%, var(--band-gold) 30%, var(--band-gold) 70%, var(--band-blue) 100%);
  }
  .headline {
    position: absolute; left: 56px; top: 36px;
    font-weight: 800; font-size: 37.5px; line-height: 46px;
    letter-spacing: 0.3px; text-transform: uppercase;
  }
  .photo { position: absolute; }
  .photo--hero {
    left: 56px; top: 135px; width: 392px; height: 261px;
    background: linear-gradient(180deg, var(--sky) 0%, #5c93de 30%, var(--snow) 42%, #d9d7d4 65%, var(--rock) 80%, #cfcfd1 100%);
  }
  .photo--flags {
    left: 56px; top: 404px; width: 125px; height: 178px;
    background: linear-gradient(135deg, var(--flag-b) 0%, var(--flag-a) 30%, #d9d5cc 50%, var(--flag-c) 72%, var(--sky) 100%);
  }
  .photo--gate {
    left: 190px; top: 404px; width: 124px; height: 178px;
    background: linear-gradient(180deg, #8a6a4a 0%, var(--stone) 40%, #e6ddd0 75%, #9c8468 100%);
  }
  .photo--mural {
    left: 324px; top: 404px; width: 124px; height: 178px;
    background: linear-gradient(90deg, #5a97df 0%, #6b5a4c 45%, var(--mural) 65%, #c9352b 100%);
  }
  .intro {
    position: absolute; left: 56px; top: 592px; width: 400px;
    font-weight: 300; font-size: 22px; line-height: 30px;
  }
  .more {
    position: absolute; left: 56px; top: 684px;
    font-weight: 700; font-style: italic; font-size: 14.5px;
  }
  .more .url { font-style: normal; }
  .more .url span { color: var(--muted); }
  .contact {
    position: absolute; left: 56px; top: 739px;
    font-weight: 700; font-size: 16.5px; line-height: 22px;
  }
  .contact span { color: var(--muted); }
  .partner-badge {
    position: absolute; left: 342px; top: 738px;
    width: 38px; height: 38px; border-radius: 50%;
    border: 2px solid var(--ink); background: var(--paper);
  }
  .brand-name {
    position: absolute; left: 392px; top: 745px; width: 60px;
    font-weight: 700; font-size: 9px; line-height: 11px;
  }
  .legal {
    position: absolute; left: 56px; top: 803px;
    font-weight: 400; font-size: 6px; color: #666;
  }
</style>
</head>
<body>
  <main class="poster">
    <h1 class="headline">Wouldn’t you<br>rather be here?</h1>

    <div class="photo photo--hero" role="img" aria-label="Snow-covered Himalayan mountain slope under a deep blue sky with two small trekkers"></div>
    <div class="photo photo--flags" role="img" aria-label="Colourful Buddhist prayer flags"></div>
    <div class="photo photo--gate" role="img" aria-label="View through a wooden doorway to a Ladakhi palace"></div>
    <div class="photo photo--mural" role="img" aria-label="Painted Buddhist mural on a monastery wall against mountains"></div>

    <p class="intro">Travel with us to Ladakh, India on a two week trekking and cultural tour. The journey of a lifetime…</p>
    <p class="more">Find out more at <span class="url">www.farridge<span>voyages</span>.example</span></p>

    <p class="contact">01632 960418<br>info@farridge<span>voyages</span>.example</p>

    <div class="partner-badge" aria-hidden="true"></div>
    <p class="brand-name">Far Ridge Voyages</p>

    <p class="legal">Disclaimer: Far Ridge Voyages is a brand name of Torrent Bend Paddle Outfitters LLP</p>

    <div class="side-band" role="img" aria-label="Vertical decorative band of Tibetan Buddhist ornaments in gold, blue, red and green"></div>
  </main>
</body>
</html>
```